Velora Crest Expo - a fashion, art, design exhibition

Please see below. The poster must be very elegant. Eventhough it has an african name and feel, it should be modern and elegant so that it attracts all types of backgrounds and races to the show.

I want this poster to be so good that it attracts Sponsors, partners and exhibitors to want to be part of the show. So its my key marketing document.

Size: A0. Good luck and be creative!

Brief is below

The VELORA CREST EXPO 2014

Dates: 19- 21 SEPTEMBER 2014:
all weekend event -open to the public
Time:
9am-5PM
OPEN TO THE PUBLIC
*Fashion shows will have exclusive show times

Venue to be confirmed

SHOWCASING
Fashion designers;
• Shoes designers;
• Accessory designers;
• Art;
• Cosmetics;
• Hair;
• Home and Décor;
• Media;
• Textiles and manufacturing;
• Technology;
• Tourism;
• Luxury/Lifestyle;
• Food & Others.

Countries representing:
SouthAfrica
Nigeria
Ghana
Kenya
Zimbabwe
Tanzania
Uganda
Ethiopia
Botswana
Mozambique
Zambia

To exhibit, partner or sponsor contact us:
Email: info@veloracrestexpo.com
Tele: 073 564 2187
Web: www.theveloracrestexpo.com
Facebook:/theveloracrestexpo
Twitter:@the veloracrestexpo

All rights reserved. Presented by Drembel International

Reason: I have extended the deadline because, one designer asked for it.

Please see the updated brief. I had alot of queries on the brief so i have shortened it.

Hi Designers,

I've attached our logo below. Please use logo version 2.1.3

We are interested in receiving more designs (right now there are only 2 to choose from)
Looking forward to your creativity.

Best regards

Hi all, Thanks for the designs that have been submitted. What i am really looking for is something that is elegant and catchy. The event/expo is an exhibition that will showcase, fashion, art, design, interior, comestics an hair etc. there will also be fashion shows that will be held on that day. It will be a nice classy event, that will draw crowds from all over Africa to participate. I have pasted the link below as a guide. Feel free to amend the brief or just use some of the info that will work. I need more designs. https://www.sample-lookup.example/search?q=example+poster+reference

Target Market(s)

The public/ in SouthA frica, Africa and the world:
-Fashion bloggers
-Magazine Editors
-Fashion Brands
-Industry experts

those who attend will want to see:

- To interact and socialise with entrepreneurs
- See what’s new
- Evaluate products and suppliers
- Keep abreast of industry and market developments
- Network/develop business contacts
Solve specific problems
- Find new markets
- Appoint agents/seek principals
- Discuss specific terms/conditions/pricing
- Consolidate business relationships

It will be an all weekend event. Adults aged 25 as per above

Industry/Entity Type

Marketing

Font styles to use
Serif

Requirements
Must have
• The poster must be elegant and appealing
Nice to have
• Be creative, think, Harbourline Style Days or Corvena style days and exhibition/trade fair combined.

The event will be fashion driven, so that lifestyle brands can also exhibit there
Should not have
• No old style

Not tacky

Must be classy

```html
<!DOCTYPE html>
<html lang="en">
<head>
<meta charset="utf-8">
<title>Velora Crest Expo 2014</title>
<link href="https://fonts.googleapis.com/css2?family=Playfair+Display:wght@700;900&family=Oswald:wght@400;600&family=Special+Elite&display=swap" rel="stylesheet">
<style>
:root{
  --sun:#f7c21b;
  --amber:#f29a0e;
  --burnt:#d8650a;
  --ember:#8a2e04;
  --cocoa:#4a1606;
  --crimson:#d21818;
  --ink:#111;
  --paper:#fff;
}
*{margin:0;padding:0;box-sizing:border-box}
html,body{width:849px;height:1200px;overflow:hidden;background:var(--paper)}
.poster{
  position:relative;width:849px;height:1200px;overflow:hidden;
  background:radial-gradient(ellipse at 70% 30%,var(--sun) 0%,var(--amber) 55%,var(--burnt) 100%);
  font-family:"Oswald",sans-serif;color:var(--ink);
}
.continent-art{
  position:absolute;right:0;top:0;width:470px;height:500px;z-index:0;
  background:radial-gradient(ellipse at 55% 40%,var(--ember) 0%,#b94a07 35%,rgba(242,154,14,0) 70%);
}
.face-art{
  position:absolute;left:0;top:830px;width:849px;height:336px;z-index:0;
  background:linear-gradient(180deg,rgba(216,101,10,0) 0%,var(--burnt) 25%,var(--ember) 65%,var(--cocoa) 100%);
}
.title{
  position:absolute;left:58px;top:122px;z-index:2;
  font-family:"Playfair Display",serif;font-weight:900;color:var(--cocoa);
  line-height:.92;letter-spacing:-1px;
}
.title .line{display:block;font-size:74px}
.title .year{display:block;font-size:44px;color:var(--crimson);margin-top:10px;letter-spacing:0;line-height:1}
.date-band{
  position:absolute;left:40px;top:486px;width:400px;height:50px;z-index:2;
  background:var(--crimson);color:var(--paper);
  font-family:"Special Elite",serif;font-size:30px;line-height:50px;padding-left:18px;white-space:nowrap;
}
.date-band sup{font-size:14px;line-height:0}
.hours{
  position:absolute;left:58px;top:546px;z-index:2;color:var(--paper);
  font-family:"Special Elite",serif;line-height:1.2;
}
.hours .when{font-size:24px;display:block}
.hours .time{font-size:28px;display:block;margin-top:4px}
.open-badge{
  position:absolute;left:57px;top:665px;width:150px;height:100px;z-index:2;
  background:var(--ink);color:var(--paper);
  font-family:"Oswald",sans-serif;font-weight:600;font-size:22px;line-height:1.05;
  padding:14px 12px;text-transform:uppercase;
}
.open-note{
  position:absolute;left:222px;top:675px;width:200px;z-index:2;color:var(--paper);
  font-family:"Special Elite",serif;font-size:18px;line-height:1.25;
}
.lineup{
  position:absolute;left:453px;top:504px;width:382px;z-index:2;
  display:grid;grid-template-columns:205px 1fr;
}
.lineup h3{
  background:var(--crimson);color:var(--paper);font-weight:600;
  font-size:15px;line-height:1.1;padding:7px 10px;text-transform:uppercase;
}
.lineup ul{list-style:none;font-size:15px;line-height:1.45;padding:8px 10px}
.lineup .showcase{color:var(--paper);text-align:right;padding-right:14px}
.lineup .countries{background:var(--ink);color:var(--paper);font-weight:600}
.contact{
  position:absolute;left:0;top:1100px;width:849px;z-index:2;text-align:center;
  color:var(--paper);font-size:13px;line-height:1.4;font-style:normal;
}
.rights{
  position:absolute;left:0;bottom:0;width:849px;height:34px;z-index:2;
  background:var(--ink);color:var(--paper);font-size:13px;
  display:flex;justify-content:space-between;align-items:center;padding:0 40px;
}
</style>
</head>
<body>
<main class="poster">
  <div class="continent-art" role="img" aria-label="Map of Africa with a painted face of an African woman set inside it"></div>
  <div class="face-art" role="img" aria-label="Close-up of eyes with tribal white dot face paint"></div>

  <h1 class="title">
    <span class="line">THE</span>
    <span class="line">VELORA</span>
    <span class="line">CREST</span>
    <span class="line">EXPO</span>
    <span class="year">2014</span>
  </h1>

  <div class="date-band">19<sup>th</sup>- 21<sup>st</sup> SEPTEMBER:</div>
  <p class="hours"><span class="when">All weekend event</span><span class="time">9AM-5PM</span></p>

  <div class="open-badge">Open<br>to the<br>public</div>
  <p class="open-note">Fashion shows will have exclusive show times</p>

  <section class="lineup">
    <h3>Showcasing</h3>
    <h3>Countries representing:</h3>
    <ul class="showcase">
      <li>Fashion designers;</li><li>• Shoes designers;</li><li>• Accessory designers;</li>
      <li>• Art;</li><li>• Cosmetics;</li><li>• Hair;</li><li>• Home and Décor;</li>
      <li>• Media;</li><li>• Textiles and manufacturing;</li><li>• Technology;</li>
      <li>• Tourism;</li><li>• Luxury/Lifestyle;</li><li>• Food &amp; Others.</li>
    </ul>
    <ul class="countries">
      <li>SouthAfrica</li><li>Nigeria</li><li>Ghana</li><li>Kenya</li><li>Zimbabwe</li>
      <li>Tanzania</li><li>Uganda</li><li>Ethiopia</li><li>Botswana</li><li>Mozambique</li><li>Zambia</li>
    </ul>
  </section>

  <address class="contact">
    To exhibit, partner or sponsor contact us: &nbsp;Email: info@veloracrestexpo.com &nbsp;Tele: 073 564 2187<br>
    Web: www.theveloracrestexpo.com &nbsp;Facebook:/theveloracrestexpo<br>
    Twitter:@the veloracrestexpo
  </address>

  <footer class="rights">
    <span>All rights reserved.</span>
    <span>Presented by Drembel International</span>
  </footer>
</main>
</body>
</html>
```